Company or website name
- Harwood & Beale LLP
- Links to the website
- harwoodbeale-example.com
- Describe your company and organization and target audience
- lawyers and clients in the need of lawyer for defective products etc
- The design should have the following
- yes
- Other Facts

```html
<!DOCTYPE html>
<html lang="en">
<head>
<meta charset="utf-8">
<title>Harwood &amp; Beale LLP</title>
<link rel="stylesheet" href="https://fonts.googleapis.com/css2?family=Arimo:wght@400;700&family=Mulish:wght@600;700;800&display=swap">
<style>
  :root {
    --navy: #0f2a63;
    --navy-text: #1a2e72;
    --nav-ink: #0d1f4d;
    --bar-grey: #a5a7aa;
    --page: #ffffff;
    --side-shadow: #8e8a8d;
    --heading-grey: #454545;
    --footer-bg: #4b4e53;
    --footer-ink: #9fa3a8;
    --panel: #e6e6e8;
  }
  * { box-sizing: border-box; margin: 0; padding: 0; }
  html, body { width: 961px; height: 1200px; overflow: hidden; background: #fff; }
  body { position: relative; font-family: "Arimo", Arial, sans-serif; }
  .abs { position: absolute; }

  .page-edge { top: 0; width: 20px; height: 1200px; }
  .page-edge--left { left: 23px; background: linear-gradient(to right, #fff, var(--side-shadow)); }
  .page-edge--right { left: 918px; background: linear-gradient(to left, #fff, var(--side-shadow)); }
  .page { left: 43px; top: 0; width: 875px; height: 1200px; background: var(--page); }

  .brand { left: 64px; top: 31px; width: 210px; font-size: 17px; line-height: 20px; font-weight: 700; color: var(--navy); letter-spacing: 0; white-space: nowrap; }

  .main-nav a { position: absolute; top: 32px; font-family: "Mulish", sans-serif; font-weight: 700; font-size: 19px; color: var(--nav-ink); text-decoration: none; white-space: nowrap; }
  .main-nav a.is-current { font-size: 22px; top: 30px; }
  .nav-bar { position: absolute; top: 59px; height: 5px; background: var(--bar-grey); }
  .nav-bar.is-current { background: var(--navy); }

  .rule { background: var(--navy); left: 43px; width: 875px; }

  .photo-lawyer { left: 160px; top: 104px; width: 130px; height: 239px; border-radius: 40px 40px 4px 4px; background: linear-gradient(#d9c9bb 0 18%, #2a2c33 18% 100%); }
  .banner { left: 313px; top: 121px; width: 486px; height: 176px; background: var(--panel); display: flex; align-items: center; justify-content: center; font-size: 38px; font-weight: 700; color: var(--navy); letter-spacing: 1px; }

  .welcome { left: 108px; top: 357px; font-size: 17px; font-weight: 700; color: var(--heading-grey); }
  .intro { color: var(--navy-text); font-weight: 700; text-transform: uppercase; line-height: 17px; font-size: 14px; width: 400px; }
  .intro .indent { display: inline-block; width: 60px; }
  .intro--small { font-size: 11.8px; line-height: 13.5px; width: 410px; }

  .login { left: 599px; top: 386px; width: 253px; height: 166px; background: #fbfbfb; }
  .login h2 { position: absolute; left: 16px; top: 6px; font-size: 16px; color: #111; }
  .login label { position: absolute; left: 10px; font-size: 15px; color: #111; }
  .login .field { position: absolute; left: 84px; width: 166px; height: 22px; border: 1px solid #c9c9c9; background: #fff; }
  .login .btn { position: absolute; left: 11px; top: 108px; width: 52px; height: 21px; border: 1px solid #9a9a9a; border-radius: 2px; background: linear-gradient(#f4f4f4, #d8d8d8); font-size: 13px; text-align: center; line-height: 19px; color: #111; }

  .feature-text { left: 114px; width: 450px; font-size: 14.5px; line-height: 17px; font-weight: 700; color: var(--navy-text); text-transform: uppercase; }
  .feature-card { left: 592px; width: 256px; height: 135px; overflow: hidden; }
  .feature-card .art { position: absolute; inset: 0; }
  .art--scales { background: linear-gradient(#5b5f66, #a6a9ad 55%, #e9e4da 78%, #2f3034); }
  .art--gavel { background: linear-gradient(120deg, #c4b9a6, #a0582a 45%, #6e3516 75%, #d9a65a); }
  .feature-card .caption { position: absolute; left: 0; bottom: 0; width: 100%; height: 24px; background: var(--navy); color: #fff; font-weight: 700; font-size: 16px; line-height: 24px; padding-left: 24px; }
  .feature-card .more { position: absolute; right: 8px; top: 5px; width: 84px; height: 21px; border-radius: 11px; background: var(--navy); border: 2px solid #fff; color: #fff; font-size: 11px; font-weight: 700; text-align: center; line-height: 17px; }

  .site-footer { left: 43px; top: 1111px; width: 875px; height: 89px; background: var(--footer-bg); }
  .footer-nav a { position: absolute; top: 1134px; font-family: "Mulish", sans-serif; font-weight: 800; font-size: 13px; color: var(--footer-ink); text-decoration: none; }
  .footer-line { left: 120px; top: 1169px; width: 732px; height: 1px; background: #5d6166; }
  .legal { left: 534px; top: 1180px; font-family: "Mulish", sans-serif; font-size: 9.5px; font-weight: 600; color: #8a8e93; word-spacing: 1px; }
</style>
</head>
<body>
  <div class="abs page-edge page-edge--left"></div>
  <div class="abs page-edge page-edge--right"></div>
  <div class="abs page"></div>

  <header>
    <div class="abs brand">HARWOOD&amp;BEALE LLP</div>
    <nav class="main-nav">
      <a class="is-current" style="left:295px">HOME</a><span class="nav-bar is-current" style="left:295px;width:60px"></span>
      <a style="left:391px">NEWS</a><span class="nav-bar" style="left:387px;width:59px"></span>
      <a style="left:480px">SERVICE</a><span class="nav-bar" style="left:479px;width:72px"></span>
      <a style="left:590px">ABOUT</a><span class="nav-bar" style="left:589px;width:61px"></span>
      <a style="left:701px">HELP</a><span class="nav-bar" style="left:689px;width:64px"></span>
      <a style="left:782px">CONTACT US</a><span class="nav-bar" style="left:782px;width:114px"></span>
    </nav>
  </header>
  <div class="abs rule" style="top:87px;height:7px"></div>

  <section class="hero">
    <div class="abs photo-lawyer" role="img" aria-label="Portrait of a partner in a dark suit and red tie"></div>
    <div class="abs banner">HARWOOD&amp;BEALE LLP</div>
    <h1 class="abs welcome">You've come to the right place.</h1>
    <p class="abs intro" style="left:111px;top:393px"><span class="indent"></span>Lorem Ipsum is simply dummy text of the printing and typesetting industry. Lorem Ipsum has been the industry's standard dummy text ever since the 1500</p>
    <p class="abs intro" style="left:111px;top:466px"><span class="indent"></span>Lorem Ipsum is simply dummy text of the printing and typesetting industry. Lorem Ipsum has been the industry's standard dummy text ever since the 1500</p>
    <p class="abs intro intro--small" style="left:108px;top:544px">Lorem Ipsum is simply dummy text of the printing and typesetting industry. Lorem Ipsum has been the industry's standard dummy text ever since the 1500</p>

    <form class="abs login">
      <h2>Customer Login</h2>
      <label style="top:46px">Username</label><span class="field" style="top:45px"></span>
      <label style="top:69px">Password</label><span class="field" style="top:68px"></span>
      <span class="btn">Login</span>
    </form>
  </section>
  <div class="abs rule" style="top:590px;height:8px;left:45px;width:873px"></div>

  <section class="features">
    <p class="abs feature-text" style="top:652px">Lorem Ipsum is simply dummy text of the printing and typesetting industry. Lorem Ipsum has been the industry's standard dummy text ever since the 1500</p>
    <div class="abs feature-card" style="top:618px">
      <div class="art art--scales" role="img" aria-label="Scales of justice against a cloudy sky"></div>
      <span class="more">READ MORE</span><span class="caption">LOREM IPSUM</span>
    </div>
    <div class="abs rule" style="top:763px;height:9px;width:879px"></div>

    <p class="abs feature-text" style="top:825px">Lorem Ipsum is simply dummy text of the printing and typesetting industry. Lorem Ipsum has been the industry's standard dummy text ever since the 1500</p>
    <div class="abs feature-card" style="top:791px">
      <div class="art art--gavel" role="img" aria-label="Wooden gavel in front of brass scales"></div>
      <span class="more">READ MORE</span><span class="caption">LOREM IPSUM</span>
    </div>
    <div class="abs rule" style="top:936px;height:9px;width:879px"></div>

    <p class="abs feature-text" style="top:998px">Lorem Ipsum is simply dummy text of the printing and typesetting industry. Lorem Ipsum has been the industry's standard dummy text ever since the 1500</p>
    <div class="abs feature-card" style="top:964px">
      <div class="art art--scales" role="img" aria-label="Scales of justice against a cloudy sky"></div>
      <span class="more">READ MORE</span><span class="caption">LOREM IPSUM</span>
    </div>
  </section>

  <footer>
    <div class="abs site-footer"></div>
    <nav class="footer-nav">
      <a style="left:83px">HOME</a>
      <a style="left:190px">NEWS</a>
      <a style="left:307px">SERVICE</a>
      <a style="left:427px">ABOUT</a>
      <a style="left:546px">HELP</a>
      <a style="left:636px">CONTACT US</a>
    </nav>
    <svg class="abs" style="left:728px;top:1124px" width="112" height="34" viewBox="0 0 112 34" aria-label="Contact links">
      <g fill="#3b3e43" stroke="#e8e8e8" stroke-width="2">
        <circle cx="18" cy="17" r="14"/><circle cx="55" cy="17" r="14"/><circle cx="93" cy="17" r="14"/>
      </g>
      <rect x="11" y="12" width="14" height="10" rx="1" fill="#fff"/>
      <path d="M11 12 L18 18 L25 12" fill="none" stroke="#3b3e43" stroke-width="1.5"/>
    </svg>
    <div class="abs footer-line"></div>
    <p class="abs legal">Privacy Policy &nbsp;|&nbsp; Terms and Conditions &nbsp;|&nbsp; © Harwood &amp; Beale 2014</p>
  </footer>
</body>
</html>
```